Business Card Design Project

We are an agricultural business based in Brisbane.
We design, manage and operate regional saleyards. Our logo is green/silver in colour and details of our business can be found on our website www.vodemarketyards.com.au

Just wanting a corporate design for some business cards and include name, position, contact details.

Thanks

Industry/Entity Type

Business

```html
<!DOCTYPE html>
<html lang="en">
<head>
<meta charset="utf-8">
<title>Vode Market Yards – Business Card</title>
<link rel="stylesheet" href="https://fonts.googleapis.com/css2?family=Questrial&display=swap">
<style>
  :root{
    --bg:#e9eaec;
    --card:#ffffff;
    --card-shade:#f1f1f1;
    --green:#0f8a43;
    --grey:#8e8f91;
    --grey-light:#c9cacb;
    --ink:#2b2b2b;
    --ink-soft:#ffffff;
  }
  *{box-sizing:border-box;margin:0;padding:0}
  html,body{width:1200px;height:900px;overflow:hidden}
  body{background:var(--bg);font-family:"Questrial",sans-serif;color:var(--ink);
    display:flex;flex-direction:column;align-items:center;justify-content:center;gap:44px}
  .card{position:relative;width:640px;height:388px;background:linear-gradient(135deg,var(--card) 40%,var(--card-shade));
    box-shadow:0 10px 28px rgba(0,0,0,.18);overflow:hidden}
  .card svg.shapes{position:absolute;inset:0;width:100%;height:100%}

  /* front */
  .front .brand{position:absolute;left:0;right:0;top:150px;text-align:center}
  .brand-name{font-size:40px;letter-spacing:1px;color:var(--ink);text-transform:uppercase;white-space:nowrap}
  .brand-mark{display:inline-block;width:14px;height:14px;background:var(--green);margin-right:12px;vertical-align:middle}

  /* back */
  .back .brand{position:absolute;left:26px;top:48px}
  .back .brand-name{font-size:20px}
  .back .brand-mark{width:9px;height:9px;margin-right:8px}
  .person{position:absolute;left:372px;top:58px;text-align:center;width:210px}
  .person-name{font-size:19px;color:var(--ink)}
  .person-role{font-size:11px;color:var(--green);margin-top:3px}
  .contacts{position:absolute;left:40px;top:238px;list-style:none;color:var(--ink-soft);font-size:15px}
  .contacts li{display:flex;align-items:center;gap:12px;height:33px}
  .contacts svg{width:13px;height:13px;fill:var(--ink-soft)}
</style>
</head>
<body>

<section class="card front">
  <svg class="shapes" viewBox="0 0 640 388" preserveAspectRatio="none">
    <rect x="0" y="0" width="640" height="22" fill="var(--grey)"/>
    <polygon points="640,150 640,388 250,388" fill="var(--green)"/>
  </svg>
  <div class="brand"><span class="brand-mark"></span><span class="brand-name">Vode Market Yards</span></div>
</section>

<section class="card back">
  <svg class="shapes" viewBox="0 0 640 388" preserveAspectRatio="none">
    <rect x="318" y="142" width="322" height="138" fill="var(--green)"/>
    <rect x="318" y="280" width="322" height="14" fill="var(--grey-light)"/>
    <rect x="0" y="225" width="318" height="118" fill="var(--grey)"/>
    <rect x="0" y="362" width="640" height="26" fill="var(--grey-light)"/>
  </svg>
  <div class="brand"><span class="brand-mark"></span><span class="brand-name">Vode Market Yards</span></div>
  <div class="person">
    <p class="person-name">Daniel Whitford</p>
    <p class="person-role">Chief Executive Officer</p>
  </div>
  <ul class="contacts">
    <li><svg viewBox="0 0 24 24"><path d="M6.6 10.8a15.1 15.1 0 0 0 6.6 6.6l2.2-2.2c.3-.3.7-.4 1-.2 1.1.4 2.3.6 3.6.6.6 0 1 .4 1 1V20c0 .6-.4 1-1 1A17 17 0 0 1 3 4c0-.6.4-1 1-1h3.5c.6 0 1 .4 1 1 0 1.3.2 2.5.6 3.6.1.3 0 .7-.2 1z"/></svg>0400 555 172</li>
    <li><svg viewBox="0 0 24 24"><path d="M12 2a10 10 0 1 0 5 18.7l-1-1.7A8 8 0 1 1 20 12v1.5a1.5 1.5 0 0 1-3 0V7h-2v1a5 5 0 1 0 .9 7.4A3.5 3.5 0 0 0 22 13.5V12A10 10 0 0 0 12 2zm0 13a3 3 0 1 1 0-6 3 3 0 0 1 0 6z"/></svg>daniel@vodemarketyards.com.au</li>
    <li><svg viewBox="0 0 24 24"><path d="M12 3 2 12h3v9h5v-6h4v6h5v-9h3z"/></svg>www.vodemarketyards.com.au</li>
  </ul>
</section>

</body>
</html>
```